Recycling Exhibition Web Design Project

We are developing a new website for a exhibition we have just taken over. The previous site is very basic and we require a complete redesign. The site should be designed to engage with and attract those who work in or provide services to the multibillion dollar wastes and recycling industry in the Asia pacific region. These will include Federal & State Governments, City councils, private sector, industry associations and other key bodies, education facilities.

KTLO is the premier waste and recycling event in the Asia Pacific region and known as place where the industry meets to share innovations, gain knowledge, to network and do business.
• Innovation
• Knowledge transfer
• Industry Networking
• Trade
Key point: need to reflect that 2012 show will attract large numbers of quality visitors from across wide range of the industry – city councils, facilities managers, etc

Site should deliver 3 key objectives.
1. Stimulate interest those who work in or provide services to the wastes and recycling industry by providing simple to access, relevant and topical information about the Expo, the Seminars, the Key Features, the sub activities and the key benefits to them.
2. Provide a platform that supports / improves EP by providing a range of interactive components – ie floor plan / video. In addition options for sales enquiries, registration, general feedback
3. Provide a way to highlight / showcase sponsors, show features and other key assets. (possibly a carousel above the fold)

We really like the dunmar website so a take on this could be good (http://www.dunmar-example.com.au/). Also we want to try to reinforce the brand so we should use the event as the hero image/banner.

Previous website - http://www.ktlo-example.com.au/

Target Market(s)

The site should be designed to engage with and attract those who work in or provide services to the multibillion dollar wastes and recycling industry

Industry/Entity Type

Recycling

Requirements
Must have
• The icons on the current site work quite well so inclusion as CTAs would be preferable.

Other key areas are

• Seminar Delegate & Visitor Registration
• Exhibitor Prospectus
• Floorplan
• Conference / Seminar content
• Social media + blog

Site visitors will need to feel like they are part of a community.
Site should reflect/display key industry stats & stats from 2011 expo

Please see the attached brief for more details and site map for menu items.

```html
<!DOCTYPE html>
<html lang="en">
<head>
<meta charset="utf-8">
<title>Pacific Resource &amp; Recycling Expo</title>
<link href="https://fonts.googleapis.com/css2?family=Cabin:ital,wght@0,400;0,600;0,700;1,400;1,600&family=Arimo:wght@400;700&display=swap" rel="stylesheet">
<style>
:root{
  --header-bg:#1f1f1f;
  --nav-bg:#3b3637;
  --nav-active:#1c1c1c;
  --accent-yellow:#f3e12b;
  --headline-orange:#e8531e;
  --quote-red:#d9231a;
  --cite-red:#b4161c;
  --body-grey:#555;
  --login-green:#7cc529;
  --support-green:#3d5a1a;
  --video-blue:#1b8fc0;
  --footer-bg:#000;
  --footer-text:#cfcfcf;
  --page-bg:#fff;
}
*{box-sizing:border-box;margin:0;padding:0}
html,body{width:958px;height:1200px;overflow:hidden;background:var(--page-bg)}
body{position:relative;font-family:"Cabin",sans-serif}
.abs{position:absolute}
.site-header{left:0;top:0;width:958px;height:115px;background:var(--header-bg)}
.brand{left:93px;top:22px;display:flex;align-items:center;gap:10px}
.brand-mark{width:34px;height:34px;border-radius:50%;background:#e2692a}
.brand-name{color:#fff;font-size:22px;font-weight:600;line-height:1.05;width:130px}
.follow{left:574px;top:20px;color:#aaa;font-size:11px;font-weight:600;display:flex;align-items:center;gap:6px}
.follow span.sq{width:14px;height:14px;background:#3a6fb4;border-radius:2px;display:inline-block}
.follow span.sq:last-child{background:#e9822c}
.search{left:714px;top:12px;width:146px;height:29px;background:#fff;border-radius:5px;border:1px solid #999;color:#aaa;font-size:12px;font-style:italic;padding:6px 9px}
.search-btn{position:absolute;right:0;top:0;width:31px;height:27px;background:#777;border-radius:0 4px 4px 0}
.login{left:742px;top:70px;width:118px;height:30px;background:var(--login-green);border:2px solid #a6e05a;border-radius:3px;color:#fff;font-weight:700;font-size:13px;text-align:center;line-height:26px}
.main-nav{left:0;top:115px;width:958px;height:37px;background:linear-gradient(#514b4c,var(--nav-bg));border-top:1px solid #6a6465}
.main-nav a{position:absolute;top:0;height:36px;line-height:36px;color:#fff;font-size:14px;text-decoration:none}
.main-nav a.current{background:var(--nav-active);color:var(--accent-yellow);padding:0 19px}
.dropdown{left:531px;top:152px;width:133px;height:35px;background:rgba(30,30,30,.85);color:#fff;font-size:13px;padding:9px 13px;z-index:3}
.hero{left:88px;top:152px;width:782px;height:263px;background:linear-gradient(#c9dde6 0%,#e6eef0 40%,#8fae4b 62%,#3f6d1e 100%);box-shadow:0 10px 14px -8px rgba(0,0,0,.35)}
.hero-title{left:88px;top:165px;width:782px;text-align:center;color:var(--headline-orange);font-size:33px;font-weight:700;letter-spacing:-.5px}
.testimonials{left:105px;top:453px;width:555px}
.testimonials h2{color:var(--quote-red);font-style:italic;font-weight:600;font-size:18px;margin-bottom:6px}
.testimonials p{color:var(--body-grey);font-size:12.6px;font-weight:600;line-height:19px}
.testimonials cite{display:block;font-style:normal;color:var(--cite-red);font-size:12.6px;font-weight:600;margin:7px 0 26px}
.media{left:691px;top:466px;width:162px;height:354px;border:1px solid #ddd;border-radius:4px}
.media-head{left:683px;top:477px;width:179px;height:35px;background:linear-gradient(#555,#1d1d1d);border-radius:4px;color:#f08a1f;font-weight:700;font-size:16px;text-align:center;line-height:35px}
.partner{position:absolute;left:700px;width:144px;display:flex;align-items:center;justify-content:center;gap:7px;font-size:14px;font-weight:600;color:#333}
.partner i{width:20px;height:20px;border-radius:50%;display:inline-block}
.video{left:104px;top:718px;width:259px;height:99px;background:linear-gradient(#34b2e0,var(--video-blue));border:1px solid #156c93;display:flex;align-items:center}
.video-icon{width:70px;height:70px;border-radius:50%;background:#8ed6f2;border:4px solid #bfe9f8;margin:0 20px 0 12px;display:flex;align-items:center;justify-content:center}
.video-label{color:#fff;font-weight:700;font-size:25px;line-height:34px}
.news{left:398px;top:718px;width:258px;height:99px;background:linear-gradient(#fff,#e3e3e3);border:1px solid #ddd;padding:4px 9px}
.news h3{font-size:18px;font-style:italic;font-weight:600;color:#111}
.news p{font-size:12px;font-style:italic;color:#888;line-height:19px;margin-top:5px}
.news .more{position:absolute;right:9px;bottom:8px;color:var(--cite-red);font-size:11px;font-style:italic}
.news .arrows{position:absolute;right:8px;top:8px;color:#999;font-size:12px}
.supported{left:103px;top:847px;color:var(--support-green);font-family:"Arimo",sans-serif;font-weight:700;font-size:15px;letter-spacing:-.2px}
.carousel{left:102px;top:876px;width:754px;height:121px;border:1px solid #ccc;border-radius:4px;background:linear-gradient(#fff 60%,#ececec);box-shadow:0 1px 4px rgba(0,0,0,.15)}
.carousel .arr{position:absolute;top:44px;color:#1e5ea8;font-size:18px;font-weight:700}
.sponsor{position:absolute;top:46px;display:flex;align-items:center;gap:6px;font-size:14px;font-weight:600}
.sponsor i{width:18px;height:18px;display:inline-block}
.site-footer{left:0;top:1023px;width:958px;height:177px;background:var(--footer-bg)}
.footer-links{left:101px;top:1036px;color:#fff;font-size:11px;font-weight:600}
.footer-links span{margin:0 4px;color:#888}
.funders{left:101px;top:1075px;width:244px;height:75px;background:#fff;border-radius:3px;display:flex;align-items:center;gap:14px;padding:0 10px}
.funders .blk{color:#1c3f8c;font-weight:700;font-size:24px}
.funders .gov{display:flex;align-items:center;gap:6px;color:#1c3f8c;font-size:11px;font-weight:600;line-height:13px}
.funders .gov i{width:18px;height:18px;background:#c8102e;display:inline-block}
.contact-title{left:562px;top:1036px;color:#ddd;font-family:"Arimo",sans-serif;font-weight:700;font-size:13px}
.contact{font-family:"Arimo",sans-serif;font-size:11px;color:var(--footer-text);line-height:18.5px}
.copyright{left:99px;top:1176px;color:#ccc;font-family:"Arimo",sans-serif;font-size:11px}
</style>
</head>
<body>
<header class="abs site-header"></header>
<div class="abs brand"><span class="brand-mark"></span><span class="brand-name">Pacific Resource &amp; Recycling Expo</span></div>
<div class="abs follow">Follow Us: <span class="sq"></span><span class="sq"></span><span class="sq" style="background:#3fb0e4"></span><span class="sq"></span></div>
<div class="abs search">Search<span class="search-btn"><svg width="31" height="27" viewBox="0 0 31 27"><circle cx="14" cy="12" r="5" fill="none" stroke="#fff" stroke-width="2"/><line x1="18" y1="16" x2="22" y2="20" stroke="#fff" stroke-width="3"/></svg></span></div>
<a class="abs login">EXHIBITOR LOGIN</a>

<nav class="abs main-nav">
  <a style="left:143px">Home</a>
  <a style="left:224px">About the Show</a>
  <a style="left:360px">What's On</a>
  <a style="left:463px">Register</a>
  <a class="current" style="left:531px">How to Exhibit</a>
  <a style="left:682px">Blog</a>
  <a style="left:748px">Contact Us</a>
</nav>
<div class="abs dropdown">Post Show Report</div>

<div class="abs hero" role="img" aria-label="Four green recycling bins labelled metal, glass, plastic and paper standing on grass"></div>
<h1 class="abs hero-title">Recycling and Sustainability?</h1>

<section class="abs testimonials">
  <h2>What our &nbsp;exhibitors and delegates have to say....</h2>
  <p>"KTLO was the perfect venue for us to launch our new organics units. In this digital era, being able to speak face-to-face and show visitors how the units work really helped them to understand the benefits. The quality and quantity of the visitors was just what we were looking for."</p>
  <cite>Round Circuit &nbsp;- 2011 Exhibitor.</cite>
  <p>"I found our firm's participation in the 2011 KTLO conference rewarding given the opportunity to engage with colleagues and potential customers in the waste to energy industry. &nbsp;My attendance has led to business leads and to continued exposure to government and private sector &nbsp;interests in other venues."</p>
  <cite>Kestrel Energy Recovery Pty Ltd - 2011 Delegate.</cite>
</section>

<aside class="abs media"></aside>
<div class="abs media-head">Media Partners</div>
<div class="partner" style="top:538px"><i style="background:#3a8fcf"></i>Green Ledger</div>
<div class="partner" style="top:626px"><i style="background:#1e9a3a"></i>Stream Review</div>
<div class="partner" style="top:740px"><i style="background:#e47ca4"></i>Reclaim Weekly</div>

<a class="abs video"><span class="video-icon"><svg width="36" height="24" viewBox="0 0 36 24"><rect x="1" y="4" width="22" height="16" rx="3" fill="#1b6f98"/><polygon points="24,12 34,5 34,19" fill="#1b6f98"/></svg></span><span class="video-label">On Demand<br>Video Library</span></a>

<div class="abs news">
  <h3>News</h3><span class="arrows">◀ ▶</span>
  <p>ResourceShow Launches a New Exhibitor Home on ResourceShow.example<br>November 8, 2011</p>
  <span class="more">Read More</span>
</div>

<h2 class="abs supported">SUPPORTED BY</h2>
<div class="abs carousel">
  <span class="arr" style="left:12px">‹</span>
  <div class="sponsor" style="left:48px;color:#1c3f8c"><i style="background:#c9a23a;border-radius:50%"></i>Municipal Alliance</div>
  <div class="sponsor" style="left:240px;color:#1a6fb5"><i style="background:#1a6fb5"></i>Resource Managers Guild</div>
  <div class="sponsor" style="left:440px;color:#9c1d22"><i style="background:#9c1d22;border-radius:50%"></i>Collectors Council</div>
  <div class="sponsor" style="left:590px;color:#1f9a3b"><i style="background:#222;border-radius:50%"></i>Coverall Systems</div>
  <span class="arr" style="right:10px">›</span>
</div>

<footer class="abs site-footer"></footer>
<div class="abs footer-links">Home<span>|</span>About the Show<span>|</span>What's on<span>|</span>Register<span>|</span>How to Exhibit<span>|</span>Blog<span>|</span>Contact Us</div>
<div class="abs funders"><span class="blk">dunmar</span><span class="gov"><i></i>State<br>Environment<br>Office</span></div>
<h3 class="abs contact-title">Contact Us</h3>
<address class="abs contact" style="left:562px;top:1059px;font-style:normal">Sam Hollis<br>Lot 9 Bracken Road,<br>Elmvale, SA, 5199<br>PO Box 482,<br>Elmvale, SA, 5199</address>
<div class="abs contact" style="left:684px;top:1060px">Phone Work/Mobile: 0400 555 123<br>Phone: 08 5550 1234<br>Fax: 08 5550 1299<br>Email: sam@elmvaleevents.example</div>
<p class="abs copyright">© 2012, Pacific Resource &amp; Recycling Expo. All Right Reserved.</p>
</body>
</html>
```